Plumbing business card and logo desgin

Need a new business card and logo for a plumbing business based in Warragul, Australia. Business name is 7Kelby plumbing & air-conditioning. We service all plumbing and gasfitting needs and installation of air-conditioning. We clear blocked drains, install new hot water systems, central heating, new and existing homes, roofing, sanitary and drainage.
i would like to have a space on there for website, email, phone, licence number and what we do as a company.
i would like a water droplet to be incorporated into the design to try and stand out that we are a plumbing business

Contact Information for Business Card

website:
phone number: 0458271936
Licence Number: 382716

Logo Text

7Kelby Plumbing & Air-Conditioning

```html
<!DOCTYPE html>
<html lang="en">
<head>
<meta charset="utf-8">
<title>7Kelby Plumbing &amp; Air-Conditioning — Business Card</title>
<link href="https://fonts.googleapis.com/css2?family=Open+Sans:wght@400;600;700;800&display=swap" rel="stylesheet">
<style>
  :root {
    --brand-blue: #1f4fd4;
    --band-grey: #7b7b7d;
    --logo-grey: #6f7073;
    --ink: #555659;
    --paper: #ffffff;
    --backdrop: #eceef1;
  }
  * { box-sizing: border-box; margin: 0; padding: 0; }
  html, body {
    width: 1200px; height: 908px; overflow: hidden;
    background: var(--backdrop);
    font-family: "Open Sans", Arial, sans-serif;
  }
  .canvas { position: relative; width: 1200px; height: 908px; }

  .card {
    position: absolute; width: 620px; height: 354px;
    overflow: hidden; box-shadow: 0 8px 24px rgba(0,0,0,.18);
  }

  /* Back of card: services */
  .card-back { left: 80px; top: 70px; background: var(--brand-blue); color: var(--paper); }
  .services-title {
    position: absolute; left: 58px; top: 52px;
    font-size: 21px; font-weight: 800; letter-spacing: 3.5px; text-transform: uppercase;
  }
  .services-list {
    position: absolute; left: 58px; top: 108px;
    display: grid; grid-template-columns: 240px 240px; column-gap: 40px;
    list-style: none;
  }
  .services-list li {
    display: flex; align-items: center; gap: 12px;
    height: 44px; font-size: 21px; font-weight: 600;
    border-bottom: 1px solid rgba(255,255,255,.18);
  }
  .checkbox { width: 13px; height: 13px; border: 1.5px solid var(--paper); flex: none; }
  .back-band {
    position: absolute; left: 0; right: 0; bottom: 0; height: 62px;
    background: var(--band-grey);
    display: flex; align-items: center; justify-content: center;
    font-size: 20px; font-weight: 700; letter-spacing: .5px;
  }

  /* Front of card: identity */
  .card-front { left: 500px; top: 480px; background: var(--paper); }
  .brand {
    position: absolute; left: 40px; top: 104px; width: 320px;
    display: flex; align-items: center; gap: 14px;
  }
  .brand-mark { width: 58px; height: 58px; border-radius: 50%; background: var(--brand-blue); flex: none; }
  .brand-name { color: var(--logo-grey); font-weight: 700; line-height: 1.1; }
  .brand-name-main { display: block; font-size: 40px; letter-spacing: 1px; }
  .brand-name-sub { display: block; font-size: 14px; letter-spacing: .4px; text-transform: uppercase; margin-top: 2px; }
  .divider {
    position: absolute; left: 384px; top: 36px; width: 2px; height: 200px;
    background: var(--brand-blue);
  }
  .contact { position: absolute; left: 404px; top: 40px; width: 206px; color: var(--ink); font-size: 13px; line-height: 1.5; }
  .contact-name { color: var(--brand-blue); font-size: 22px; font-weight: 700; margin-bottom: 6px; }
  .contact-row { display: flex; align-items: center; gap: 7px; margin-top: 6px; white-space: nowrap; }
  .contact-row svg { width: 15px; height: 15px; flex: none; }
  .licence { margin-top: 8px; }
  .front-band {
    position: absolute; left: 0; right: 0; bottom: 0; height: 72px;
    background: var(--brand-blue); color: var(--paper);
    display: flex; align-items: center; justify-content: center;
    font-size: 22px; font-weight: 700; letter-spacing: .5px;
  }
</style>
</head>
<body>
<main class="canvas">

  <section class="card card-back" aria-label="Business card back">
    <h2 class="services-title">Mechanical Pumbing Services</h2>
    <ul class="services-list">
      <li><span class="checkbox"></span>Make Good</li>
      <li><span class="checkbox"></span>Plant Room Works</li>
      <li><span class="checkbox"></span>Refurbishment</li>
      <li><span class="checkbox"></span>Shut Downs</li>
      <li><span class="checkbox"></span>Tenancy Fit Out</li>
      <li><span class="checkbox"></span>Change Overs</li>
    </ul>
    <div class="back-band">www.7kelbyplumbing.com</div>
  </section>

  <section class="card card-front" aria-label="Business card front">
    <div class="brand">
      <span class="brand-mark"></span>
      <p class="brand-name">
        <span class="brand-name-main">7Kelby</span>
        <span class="brand-name-sub">Plumbing &amp; Air-Conditioning</span>
      </p>
    </div>
    <div class="divider"></div>
    <div class="contact">
      <p class="contact-name">Jordan Pellow</p>
      <p>42 Harlow Lane<br>Warragul, VIC 3820</p>
      <p class="contact-row">
        <svg viewBox="0 0 16 16" aria-hidden="true"><circle cx="8" cy="8" r="7" fill="none" stroke="#555659" stroke-width="1.2"/><path d="M5.3 4.5l1.4 1.4-.8 1.1c.5 1 1.3 1.8 2.3 2.3l1.1-.8 1.4 1.4-.9 1.1c-2.6-.5-4.6-2.5-5.1-5.1z" fill="#555659"/></svg>
        045 827 1936
      </p>
      <p class="contact-row">
        <svg viewBox="0 0 16 16" aria-hidden="true"><circle cx="8" cy="8" r="7" fill="none" stroke="#555659" stroke-width="1.2"/><rect x="4" y="5.3" width="8" height="5.6" fill="none" stroke="#555659" stroke-width="1"/><path d="M4 5.5l4 3 4-3" fill="none" stroke="#555659" stroke-width="1"/></svg>
        jordan@7kelbyplumber.com
      </p>
      <p class="licence">Lic : 382716</p>
    </div>
    <div class="front-band">www.7kelbyplumbing.com</div>
  </section>

</main>
</body>
</html>
```